High Tech Real Estate Startup needs a business card

We are developing an innovative real estate marketing product based around advanced search and virtual reality.

We talk to people, we need business cards.

Target Market(s)

The target market is technology professionals and realtors.

Contact Information for Business Card

The information to be included will include

Name
Title
Phone Number
E-mail Address
www.plindo.com

It should use simple iconography for each one of those fields.

Font styles to use
Other font styles liked:
• Co, Jubilat, Avenir

Colors

Designer to choose colors to be used in the design.

Requirements
Must have
• Clean aesthetic,
• Good use of negative space.
• It should use our company logo, shown in the attached file. It is able to use the negative of that logo (coloured font and white background) and I have attached other acceptable accent colours in a swatch file.
Should not have
• Should not be too busy
• No extraneous text (slogans, tag lines etc)

```html
<!DOCTYPE html>
<html lang="en">
<head>
<meta charset="utf-8">
<title>Plindo Business Card</title>
<link href="https://fonts.googleapis.com/css2?family=Lato:wght@400;700&display=swap" rel="stylesheet">
<style>
  :root {
    --backdrop: #111111;
    --brand-teal: #03babf;
    --paper: #ffffff;
    --ink: #2b2b2b;
  }
  html, body {
    margin: 0;
    padding: 0;
    width: 1200px;
    height: 900px;
    overflow: hidden;
    background: var(--backdrop);
    font-family: "Lato", Arial, sans-serif;
  }
  .stage {
    position: relative;
    width: 1200px;
    height: 900px;
  }
  .card {
    position: absolute;
    top: 306px;
    width: 440px;
    height: 271px;
    box-shadow: 0 2px 6px rgba(0,0,0,0.5);
  }
  .card--front { left: 149px; background: var(--paper); }
  .card--back  { left: 608px; background: var(--brand-teal); height: 272px; }

  .brand-block {
    position: absolute;
    display: flex;
    align-items: center;
    justify-content: center;
    font-weight: 400;
    font-size: 24px;
    letter-spacing: 1px;
  }
  .card--front .brand-block {
    left: 50px; top: 71px;
    width: 130px; height: 129px;
    background: var(--brand-teal);
    color: var(--paper);
  }
  .card--back .brand-block {
    left: 158px; top: 74px;
    width: 125px; height: 124px;
    background: var(--paper);
    color: var(--brand-teal);
  }

  .details {
    position: absolute;
    left: 215px;
    top: 83px;
  }
  .details__name {
    margin: 0;
    font-size: 19px;
    font-weight: 700;
    color: var(--brand-teal);
    line-height: 24px;
  }
  .details__title {
    margin: 0 0 12px;
    font-size: 13px;
    color: var(--ink);
    line-height: 16px;
  }
  .contact-list {
    list-style: none;
    margin: 0;
    padding: 0;
  }
  .contact-list li {
    display: flex;
    align-items: center;
    font-size: 13px;
    color: var(--ink);
    line-height: 16.5px;
  }
  .contact-list svg {
    width: 12px;
    height: 12px;
    margin: 0 4px 0 2px;
    fill: var(--brand-teal);
  }
</style>
</head>
<body>
<main class="stage">
  <section class="card card--front">
    <div class="brand-block">PLINDO</div>
    <div class="details">
      <h1 class="details__name">DANIEL HARPER</h1>
      <p class="details__title">MANAGING DIRECTOR</p>
      <ul class="contact-list">
        <li>
          <svg viewBox="0 0 12 12" aria-hidden="true"><path d="M1 4.2C1 2.6 3 1.8 6 1.8s5 .8 5 2.4v.9H8.4v-1H3.6v1H1zM3.2 5.5h5.6l1.6 4.7H1.6zM6 6.6a1.3 1.3 0 1 0 0 2.6 1.3 1.3 0 0 0 0-2.6z"/></svg>
          444 555 7120
        </li>
        <li>
          <svg viewBox="0 0 12 12" aria-hidden="true"><path d="M1 2.5h10v7H1zM2 3.4v.4l4 2.7 4-2.7v-.4zM2 4.9v3.7h8V4.9L6 7.6z"/></svg>
          HELLO@PLINDO.COM
        </li>
        <li>
          <svg viewBox="0 0 12 12" aria-hidden="true"><circle cx="6" cy="6" r="5"/><path d="M3 3.5l1.5.3.6 1.3-1 .8.3 1.6-1.2-1zM7 2.2l1.6.6.2 1.4-1.2.3zM6.8 6.5l1.8.3.4 1.6-1.3 1.4-.6-1.7z" fill="#ffffff"/></svg>
          WWW.PLINDO.COM
        </li>
      </ul>
    </div>
  </section>

  <section class="card card--back">
    <div class="brand-block">PLINDO</div>
  </section>
</main>
</body>
</html>
```